Upbeat Accouting Package Flyer

I am looking for a 1 page (front, or front and back) flyer that will become our marketing for our accounting services. We are looking for something a little different and we are catering to the small retail shop owners. We have 3 accounting packages we would like to display and then some add-ons. I have included our logo that must be included in the design. I have uploaded the accounting package information as well.
Target Market(s)
Small Retail Shop Owners
Industry/Entity Type
Accounting
Colors
Designer to choose colors to be used in the design.
Requirements
Must have
- A casual feel. We are not your typical accountants who are very professional and "stuffy". I want it to feel like we are all family.
Nice to have
- I would like to incorporate some sort of retail theme.
- We have a couple of taglines we like to use and it would be great if they could be included. They are "We know you CAN do the accounting, but do you WANT to?" and "We allow you to get back to what's important."
Should not have
- Typical stock accounting photos of people shaking hands, large office buildings, etc.

```html
<!DOCTYPE html>
<html lang="en">
<head>
<meta charset="UTF-8">
<title>Larkfield Accounting Packages Flyer</title>
<link href="https://fonts.googleapis.com/css2?family=Arimo:wght@400;700&family=Caveat+Brush&display=swap" rel="stylesheet">
<style>
  :root {
    --page-bg: #ffffff;
    --ink: #1d1d1f;
    --frame: #6d6e71;
    --teal: #1fb3b0;
    --develop: #4a8fca;
    --develop-soft: #d2e2f1;
    --grow: #63c46f;
    --grow-soft: #c4e9c8;
    --relax: #fbbe67;
    --relax-soft: #fde1b4;
    --options: #a7a9ac;
    --brand: #3a3b3d;
    --photo-warm: #b07a4a;
    --photo-deep: #2e4850;
  }
  * { margin: 0; padding: 0; box-sizing: border-box; }
  html, body {
    width: 1200px; height: 1000px; overflow: hidden;
    background: var(--page-bg);
    font-family: "Arimo", Arial, sans-serif;
    color: var(--ink);
  }
  .flyer {
    position: absolute; left: 302px; top: 62px;
    width: 597px; height: 843px;
    border: 1px solid var(--frame);
    background: #fff;
  }
  .hero-photo {
    position: absolute; left: 0; top: 0; width: 595px; height: 340px;
    background:
      radial-gradient(ellipse at 75% 30%, rgba(230,200,160,.6), transparent 55%),
      linear-gradient(180deg, var(--photo-deep) 0%, #5c5a55 45%, var(--photo-warm) 75%, #8a5a35 100%);
  }
  .tagline {
    position: absolute; left: 0; top: 350px; width: 595px;
    text-align: center;
    font-family: "Caveat Brush", cursive;
    font-size: 38px; line-height: 40px;
    color: var(--ink);
  }
  .section-band {
    position: absolute; left: 16px; top: 445px; width: 564px; height: 30px;
    background: linear-gradient(90deg, rgba(31,179,176,0) 0%, var(--teal) 35%, var(--teal) 65%, rgba(31,179,176,0) 100%);
    color: #fff; text-align: center;
    font-size: 20px; line-height: 30px; font-weight: 400;
  }
  .packages { position: absolute; left: 13px; top: 484px; display: flex; gap: 6px; }
  .package { width: 185px; height: 252px; border-radius: 0 0 8px 8px; overflow: hidden; }
  .package-title {
    height: 36px; line-height: 36px; text-align: center;
    color: #fff; font-size: 17px;
  }
  .package-body { padding: 10px 10px 0 16px; font-size: 9.6px; line-height: 12px; }
  .package-body .price b { font-weight: 700; }
  .package-body ul { list-style: none; }
  .package-body li { position: relative; padding-left: 8px; }
  .package-body li::before { content: "•"; position: absolute; left: 0; }
  .develop .package-title { background: var(--develop); }
  .develop { background: var(--develop-soft); }
  .grow .package-title { background: var(--grow); }
  .grow { background: var(--grow-soft); }
  .relax .package-title { background: var(--relax); }
  .relax { background: var(--relax-soft); }
  .add-ons {
    position: absolute; left: 13px; top: 749px; width: 307px; height: 81px;
    background: var(--options); border-radius: 8px;
    color: #fff; padding: 10px 17px; font-size: 10px; line-height: 12px;
  }
  .add-ons h3 { font-size: 10px; font-weight: 700; }
  .brand {
    position: absolute; left: 350px; top: 760px;
    display: flex; align-items: center; gap: 10px;
  }
  .brand-dot { width: 14px; height: 14px; border-radius: 50%; background: var(--teal); }
  .brand-name { font-size: 42px; font-weight: 700; color: var(--brand); letter-spacing: .5px; }
</style>
</head>
<body>
  <main class="flyer">
    <div class="hero-photo" role="img" aria-label="Photo of three smiling women chatting over coffee at a café table with notebooks and phones"></div>

    <h1 class="tagline">We know you CAN do the<br>accounting, but do you WANT to?</h1>

    <h2 class="section-band">Accounting Packages</h2>

    <section class="packages">
      <article class="package develop">
        <div class="package-title">Develop</div>
        <div class="package-body">
          <p class="price"><b>$300/mo</b> when paid annually</p>
          <p class="price"><b>$325/mo</b> billed monthly</p>
          <ul>
            <li>LedgerLine Online subscription</li>
            <li>Free accounting setup</li>
            <li>Weekly transaction processing</li>
            <li>Monthly account reconciliation (up to 2 accounts)</li>
            <li>Monthly financial statements by the 15th of the month</li>
          </ul>
        </div>
      </article>
      <article class="package grow">
        <div class="package-title">Grow</div>
        <div class="package-body">
          <p class="price"><b>$550/mo</b> billed annually;</p>
          <p class="price"><b>$575/mo</b> billed monthly</p>
          <ul>
            <li>LedgerLine Online subscription</li>
            <li>Free accounting setup</li>
            <li>Weekly transaction processing</li>
            <li>Monthly account reconciliation (up to 4 accounts)</li>
            <li>Monthly financial statements by the 10th of the month</li>
            <li>Client portal access for document sharing</li>
            <li>1 Custom Report</li>
            <li>Accounts Payable</li>
            <li>Monthly Scorecard (customized metric tracking for your business)</li>
          </ul>
        </div>
      </article>
      <article class="package relax">
        <div class="package-title">Relax (We've Got This)</div>
        <div class="package-body">
          <p class="price"><b>$850/mo</b> billed annually;</p>
          <p class="price"><b>$875/mo</b> billed monthly</p>
          <ul>
            <li>LedgerLine Online subscription</li>
            <li>Free accounting setup</li>
            <li>Weekly transaction processing</li>
            <li>Monthly account reconciliation (up to 5-10 accounts)</li>
            <li>Monthly financial statements by the 5th of the month</li>
            <li>Client portal access for document sharing</li>
            <li>2 Custom Reports</li>
            <li>Accounts Payable</li>
            <li>Invoicing and accounts receivable</li>
            <li>Weekly Scorecard (customized metric tracking for your business)</li>
          </ul>
        </div>
      </article>
    </section>

    <aside class="add-ons">
      <h3>Additional Options</h3>
      <p>Payroll – 1-10 employees $85/mo; 11-30 employees $175/mo</p>
      <p>Sales tax - $30/mo per state</p>
      <p>Corporate taxes $50/mo</p>
      <p>Owner taxes - $25/mo</p>
    </aside>

    <div class="brand">
      <span class="brand-dot"></span>
      <span class="brand-name">Larkfield</span>
    </div>
  </main>
</body>
</html>
```